Magician | Speaker looks for an innovative business card design

I'm a magician and public speaker offering artistic and modern magical experiences.
I'm based in Brussels (Belgium.) I love magic performed up-close, creating a space of intimacy, even when I'm on stage.
The final design should communicate professionalism, elegance, artistry, and a friendly kind personality

I would like to see designs based either on my photos and/or the way I sign my name Remy Vok (see attached files for more info.)
Additional photos and more info about what I offer can be seen at www.remy-vok.net

My current business card design is also attached. I like the fact that the reverse of my current design includes quotes from master magicians about magic, changing the way my participants see the art of magic.

Note: I would like a double-sided card design. However, I need white space on the reverse to be able to write things on for my performances.

Details to include on the card:
Artist name: Remy Vok
Offer: magician + (public) speaker or magic + (public) speaking (the + sign can be replaced by another character, like a bullet or a pipe)
Phone: +32 471 265 903
Email: book@remy-vok.net
(optional) Website: www.remy-vok.net or remy-vok.net

Target Market(s)

Corporate, organisations, companies as well as individuals

Industry/Entity Type

Artists

Colors

Designer to choose colors to be used in the design.

Requirements
Nice to have
• A side with a mirror could be nice

```html
<!DOCTYPE html>
<html lang="en">
<head>
<meta charset="utf-8">
<title>Remy Vok – Business Card</title>
<link href="https://fonts.googleapis.com/css2?family=Open+Sans:wght@400&family=Roboto+Condensed:wght@400&display=swap" rel="stylesheet">
<style>
  :root {
    --backdrop: #728387;
    --card-paper: #eaf3f1;
    --mint: #d8fdf6;
    --orange: #ff6f0d;
    --green: #49a736;
    --pink: #ff3ddc;
    --blue: #3956c7;
    --ink: #111111;
    --white: #ffffff;
  }
  * { margin: 0; padding: 0; box-sizing: border-box; }
  html, body { width: 1200px; height: 1200px; overflow: hidden; }
  body {
    background: var(--backdrop);
    position: relative;
    font-family: "Open Sans", Arial, sans-serif;
  }
  .card {
    position: absolute;
    top: 171px;
    width: 540px;
    height: 899px;
    background: var(--card-paper);
  }
  .card--front { left: 30px; }
  .card--back { left: 638px; }

  .front-name {
    position: absolute;
    left: 0; top: 0;
    width: 540px; height: 235px;
    display: flex; align-items: center; justify-content: center;
    font-size: 74px;
    color: var(--ink);
    letter-spacing: 1px;
  }
  .band {
    position: absolute;
    left: 0;
    width: 540px;
    height: 156px;
    display: flex; align-items: center;
    color: var(--white);
    font-size: 34px;
    white-space: nowrap;
  }
  .band--phone { top: 235px; background: var(--orange); padding-left: 14px; font-size: 40px; letter-spacing: 1px; }
  .band--email { top: 402px; background: var(--green); justify-content: center; }
  .band--web { top: 568px; background: var(--pink); justify-content: center; }
  .band--role { top: 735px; background: var(--blue); justify-content: center; font-size: 40px; }
  .dot { display: inline-block; width: 18px; height: 18px; border-radius: 50%; background: var(--white); margin: 0 16px; vertical-align: middle; }

  .back-header {
    position: absolute;
    left: 8px; top: 7px;
    width: 524px; height: 428px;
    background: var(--mint);
    text-align: center;
  }
  .back-name {
    position: absolute;
    left: 0; right: 0; top: 170px;
    font-size: 44px;
    color: var(--ink);
  }
  .back-role {
    position: absolute;
    left: 0; right: 0; top: 246px;
    font-family: "Roboto Condensed", "Arial Narrow", sans-serif;
    font-size: 20px;
    color: var(--ink);
  }
  .back-role .dot { width: 8px; height: 8px; background: var(--ink); margin: 0 5px; }
  .photo { position: absolute; }
  .photo--portrait {
    left: 8px; top: 443px; width: 300px; height: 448px;
    background: radial-gradient(ellipse at 55% 45%, #3a2a26 0%, #17110f 55%, #050505 100%);
  }
  .photo--coin {
    left: 315px; top: 443px; width: 217px; height: 222px;
    background: linear-gradient(135deg, #6a1a2c 0%, #2a1418 50%, #15181e 100%);
  }
  .photo--cards {
    left: 315px; top: 670px; width: 217px; height: 221px;
    background: linear-gradient(160deg, #1f3452 0%, #16263d 60%, #0d1726 100%);
  }
</style>
</head>
<body>
  <section class="card card--front">
    <div class="front-name">Remy Vok</div>
    <div class="band band--phone">Phone: +32 471 265 903</div>
    <div class="band band--email">book@remy-vok.net</div>
    <div class="band band--web">www.remy-vok.net</div>
    <div class="band band--role">magician<span class="dot"></span>public speaker</div>
  </section>

  <section class="card card--back">
    <div class="back-header">
      <div class="back-name">Remy Vok</div>
      <div class="back-role">MAGICIAN<span class="dot"></span>PUBLIC SPEAKER</div>
    </div>
    <div class="photo photo--portrait" role="img" aria-label="Portrait photo of the magician seated in a dark jacket against a brick wall"></div>
    <div class="photo photo--coin" role="img" aria-label="Photo of a hand holding up coins between the fingers"></div>
    <div class="photo photo--cards" role="img" aria-label="Photo of hands springing playing cards"></div>
  </section>
</body>
</html>
```